eBook book cover for erotic novel set in Singapore (yes really!)

Hello - here’s a bit of background on my book, along with some thoughts on the cover. I hope this helps; am happy to answer any questions and provide further example chapters if that would help you get a better idea of what it’s all about (some extracts are attached to this brief).

1. "Under Quiet Lanterns" - synopsis
“I'm curious—and tempted. Oh dear!” is Bea’s reply to an advert posted on the internet and she enters into a relationship unlike any other she has experienced before—one that stimulates, frustrates, consumes and ultimately, delights, her.

Owen a successful banker living in Singapore has placed an online invitation for “irregular intimacy” with a “sexy, well-dressed lover with stimulating kinks”. Bea’s feeling dulled by her demanding job and the undemanding social rituals of her life in Singapore: she’s attracted to Owen’s slightly jaded urbanity and quirky ways. He finds her plain-speaking exuberance a refreshing contrast to his own more conservative nature.

After a sparky, and at times, spiky, email exchange they meet at a rooftop bar in Singapore’s Chinatown. Over cocktails they agree the seven rules of their relationship (the first one—“No questions about work or personal lives”). Despite this formality, the sexual attraction between them is intense—as is the sex when they first manage to schedule it. Over subsequent weeks they craft a list of sexual experiences they intend to enjoy together. Once they’ve completed ‘The List’ (on an Excel spreadsheet) they’ll part. That’s the intention anyway.

As their relationship develops they both can’t help applying their controlling corporate selves to their secret life. Apart from the proposed experiences on the agreed list, each of them sometimes introduces new things to surprise the other. Under Quiet Lanterns is set mainly in Singapore—where the exotic sights, sounds and tastes provide a sensual backdrop to the increasingly intense affair.

The novel is about two people who believe they can manage their relationship in the same way they organise everything else in their lives—with closely calibrated calendar entries, tightly planned sexual liaisons and multiple lists. They relish the contrasts between their demanding jobs (the frequent travel, late night conference calls and always-on Quillphones) and indulging their imaginations with someone they trust. Bea begins to appreciate just what being “sex fit” entails. The sex scenes are explicit (“Sex where she did things she couldn’t tell her sisters about”) and driven in part by their competitive natures.

However, it gradually becomes clear that it is becoming harder for them to contain their relationship to just sex, no matter how delightful. They had both originally committed to a ‘no strings attached’ affair but they struggle with their growing feelings for each other. Owen initially drives the relationship but increasingly becomes out of his depth whilst Bea gains confidence. The novel ends with over half The List still to be completed—will they be able to keep to the rules, and more importantly, maintain the expected emotional distance they’ve both agreed to?

2. Cover thoughts
I’d like to avoid the typical cliched image of say, a silk tie and handcuffs, that one often sees on book covers of this genre. A reference to Singapore/Asia would be good of course (an orchid too obvious?), and naturally being an ebook, the cover needs to be simple and striking. I have a second book planned, and half written, and possibly a third. A design that thus lends itself to being adapted slightly so as to support a trilogy would be particularly useful.

3. Author's name
Gus Palmer

Thanks
Gus

Women 25-45

Serif
Decorative
Script

85cae6
3176b5

• A reference to Asia/Singapore
• A sense of the unknown, reference to Asia/Singapore, a hint of sex attraction, reference to corporate life.
• Just had a thought that a single stiletto shoe (on a carpet, wooden floorboards?) might be interesting.
• Be overly explicit sexually - have the usual cliche of a scantily clad woman for example

```html
<!DOCTYPE html>
<html lang="en">
<head>
<meta charset="utf-8">
<title>Under Quiet Lanterns — Book Cover Wrap</title>
<link rel="stylesheet" href="https://fonts.googleapis.com/css2?family=Jost:wght@300;400;500;700&family=Oswald:wght@600&display=swap">
<style>
  :root {
    --page-bg: #e8edf1;
    --sky-light: #e4f2f9;
    --sky-mid: #bfe0ef;
    --sky-deep: #85cae6;
    --brand-blue: #3176b5;
    --ink-blue: #2d6fae;
    --title-light: #4c8fc6;
    --back-ink: #1f3f5c;
    --panel-fill: rgba(255, 255, 255, 0.42);
    --panel-edge: rgba(255, 255, 255, 0.7);
    --accent-red: #d2452e;
    --cream: #f3ebdc;
  }

  * { margin: 0; padding: 0; box-sizing: border-box; }

  html, body {
    width: 1200px;
    height: 835px;
    overflow: hidden;
    background: var(--page-bg);
  }

  .cover-wrap {
    position: absolute;
    left: 165px;
    top: 97px;
    width: 870px;
    height: 640px;
    display: flex;
    box-shadow: 0 18px 40px rgba(30, 50, 70, 0.18);
  }

  /* Back cover */
  .back-cover {
    position: relative;
    width: 400px;
    height: 100%;
    background:
      radial-gradient(circle at 20% 18%, rgba(255,255,255,0.55) 0, rgba(255,255,255,0) 22%),
      radial-gradient(circle at 78% 35%, rgba(70,150,200,0.55) 0, rgba(70,150,200,0) 26%),
      radial-gradient(circle at 30% 70%, rgba(40,120,180,0.45) 0, rgba(40,120,180,0) 28%),
      radial-gradient(circle at 80% 85%, rgba(255,255,255,0.5) 0, rgba(255,255,255,0) 20%),
      linear-gradient(160deg, var(--sky-mid), var(--sky-deep) 55%, #5fa8d2);
  }

  .blurb-panel {
    position: absolute;
    left: 28px;
    top: 36px;
    right: 28px;
    bottom: 44px;
    border-radius: 14px;
    background: var(--panel-fill);
    border: 1px solid var(--panel-edge);
    padding: 90px 22px 0;
    text-align: center;
  }

  .blurb-panel p {
    font-family: "Jost", sans-serif;
    font-weight: 400;
    font-size: 13.5px;
    line-height: 1.72;
    color: var(--back-ink);
    margin-bottom: 18px;
  }

  /* Spine */
  .spine {
    position: relative;
    width: 70px;
    height: 100%;
    background: linear-gradient(90deg, #a9d6ea, var(--sky-light) 45%, #b6dcee);
    display: flex;
    flex-direction: column;
    align-items: center;
  }

  .spine-author {
    margin-top: 14px;
    width: 58px;
    padding: 4px 0;
    background: var(--brand-blue);
    color: #fff;
    font-family: "Jost", sans-serif;
    font-weight: 500;
    font-size: 10px;
    text-align: center;
    letter-spacing: 0.3px;
  }

  .spine-title {
    margin-top: 26px;
    writing-mode: vertical-rl;
    font-family: "Oswald", sans-serif;
    font-weight: 600;
    font-size: 34px;
    letter-spacing: 5px;
    color: var(--brand-blue);
    text-transform: uppercase;
  }

  /* Front cover */
  .front-cover {
    position: relative;
    width: 400px;
    height: 100%;
    background: linear-gradient(170deg, var(--sky-light) 0%, var(--sky-mid) 50%, #9fd0e8 100%);
    text-align: center;
  }

  .cover-photo {
    position: absolute;
    left: 90px;
    top: 30px;
    width: 270px;
    height: 360px;
    border-radius: 6px;
    background:
      radial-gradient(ellipse at 45% 60%, rgba(243,235,220,0.9) 0, rgba(243,235,220,0) 45%),
      radial-gradient(ellipse at 70% 55%, rgba(210,69,46,0.35) 0, rgba(210,69,46,0) 35%),
      linear-gradient(180deg, rgba(255,255,255,0.25), rgba(255,255,255,0));
  }

  .title-top {
    position: absolute;
    left: 0;
    right: 0;
    top: 418px;
    font-family: "Jost", sans-serif;
    font-weight: 300;
    font-size: 40px;
    letter-spacing: 2px;
    color: var(--title-light);
    text-transform: uppercase;
  }

  .title-main {
    position: absolute;
    left: 0;
    right: 0;
    top: 462px;
    font-family: "Jost", sans-serif;
    font-weight: 700;
    font-size: 70px;
    letter-spacing: 1px;
    line-height: 1;
    text-transform: uppercase;
    background: linear-gradient(180deg, #4a86c4 0%, #2a5f9a 55%, #6e8fd0 100%);
    -webkit-background-clip: text;
    background-clip: text;
    color: transparent;
  }

  .author-name {
    position: absolute;
    left: 0;
    right: 0;
    top: 556px;
    font-family: "Jost", sans-serif;
    font-weight: 500;
    font-size: 30px;
    letter-spacing: 1px;
    color: var(--ink-blue);
    text-transform: uppercase;
  }
</style>
</head>
<body>
  <main class="cover-wrap">
    <section class="back-cover">
      <div class="blurb-panel">
        <p>Books may also refer to works of literature, or a main division of such a work. In library and information science, a book is called a monograph, to distinguish it from serial periodicals such as magazines, journals or newspapers. The body of all written works including books is literature. In novels and sometimes other types of books (for example, biographies), a book may be divided into several large sections, also called books (Book 1, Book 2, Book 3, and so on). An avid reader of books is a bibliophile or colloquially, bookworm.</p>
        <p>A shop where books are bought and sold is a bookshop or bookstore. Books can also be borrowed from libraries. Lumenfind has estimated that as of 2010, approximately 130,000,000 unique titles had been published</p>
      </div>
    </section>

    <section class="spine">
      <div class="spine-author">GUS PALMER</div>
      <div class="spine-title">Under Quiet Lanterns</div>
    </section>

    <section class="front-cover">
      <div class="cover-photo" role="img" aria-label="A woman's hand dangling a single cream and red stiletto shoe from one finger against a pale blue sky"></div>
      <h1>
        <span class="title-top">Under Quiet</span>
        <span class="title-main">Lanterns</span>
      </h1>
      <p class="author-name">Gus Palmer</p>
    </section>
  </main>
</body>
</html>
```